Hedge fund needs power point design for marketing pitch

We need a designer to make our power point pitch more aesthetically appealing to potential clients. We will be marketing our hedge fund to high net worth individuals and financial institutions. The ideal design will look professional and project confidence to our potential clients. We have attached a rough outline of what we have completed so far. We have also attached example cover pages for 2 pitch books produced by our competitors.

Target Market(s)

Financial institutions and wealthy investors

Industry/Entity Type

Finance

Requirements
Must have
• must use our logo and current slides. Must look professional

```html
<!DOCTYPE html>
<html lang="en">
<head>
<meta charset="utf-8">
<title>Fund Pitch Slides</title>
<link href="https://fonts.googleapis.com/css2?family=Mulish:wght@400;600;700&display=swap" rel="stylesheet">
<style>
:root{
  --canvas:#ececee;
  --slide-bg:#eef3f9;
  --slide-glow:#d6e4f2;
  --band-blue:#3f7cc4;
  --band-blue-dark:#2f68ad;
  --gold:#c08a1e;
  --gold-light:#e5c15a;
  --green-dark:#0f2f23;
  --ink:#1b1b1b;
  --red:#e0231c;
  --table-line:#b9872a;
}
*{box-sizing:border-box;margin:0;padding:0}
html,body{width:1200px;height:1200px;overflow:hidden}
body{background:var(--canvas);font-family:"Mulish",sans-serif;color:var(--ink);position:relative}
.slide{position:absolute;width:546px;height:408px;overflow:hidden;
  background:radial-gradient(ellipse at 70% 30%,var(--slide-glow) 0%,var(--slide-bg) 45%,#f6f8fb 100%)}
.slide .backdrop{position:absolute;inset:0;
  background:radial-gradient(circle at 62% 22%,rgba(170,195,222,.45) 0%,rgba(170,195,222,0) 38%)}
.slide .base{position:absolute;left:0;right:0;bottom:0;height:20px}
.slide .base::before{content:"";position:absolute;left:0;right:0;top:0;height:12px;
  background:linear-gradient(90deg,var(--gold) 0%,var(--gold-light) 55%,var(--gold) 100%)}
.slide .base::after{content:"";position:absolute;left:0;right:0;bottom:0;height:8px;background:var(--green-dark)}
.s-tl{left:48px;top:156px}.s-tr{left:627px;top:156px}
.s-bl{left:48px;top:604px}.s-br{left:627px;top:604px}

.band{position:absolute;left:0;background:linear-gradient(180deg,var(--band-blue),var(--band-blue-dark));color:#fff;
  display:flex;align-items:center;box-shadow:2px 2px 0 rgba(255,255,255,.5);font-weight:400}
.band-sim{top:17px;height:51px;padding-left:32px;font-size:12.4px;white-space:nowrap;overflow:hidden}
.s-tl .band-sim{width:492px}
.s-tr .band-sim{width:537px;padding-left:32px;font-size:11.2px}
.band-big{top:26px;height:52px;padding-left:33px;font-size:31px;letter-spacing:.2px;white-space:nowrap}
.s-bl .band-big{width:342px}.s-br .band-big{width:323px}

.chart{position:absolute;left:44px;top:78px;width:194px;height:141px;background:#e9ebed}
.s-tr .chart{top:80px;width:195px;height:138px}
.chart svg{display:block}

.facts{position:absolute;left:279px;top:94px;width:240px;font-size:10.2px;line-height:12.8px;list-style:none}
.facts li{position:relative;padding-left:16px}
.facts li::before{content:"•";position:absolute;left:0}
.s-tr .facts{top:98px;width:250px}

.stats{position:absolute;left:13px;top:237px;width:521px;border:1px solid var(--table-line);background:var(--gold)}
.s-tr .stats{left:14px;top:238px;width:520px}
.stats table{width:100%;border-collapse:collapse;font-size:6.4px;table-layout:fixed}
.stats th{color:#fff;font-weight:700;height:9px;line-height:9px}
.stats thead tr:first-child th{text-align:center}
.stats .cols th{background:var(--green-dark);border-right:1px solid #fff}
.stats td{background:#fff;border:1px solid #d8c08a;text-align:right;padding-right:3px;height:9.8px;line-height:9px;white-space:nowrap;overflow:hidden}
.stats td.period{text-align:center;font-weight:700}
.stats td.hl{color:var(--red)}
.stats .note{color:#fff;font-size:6.5px;line-height:11px;padding:1px 2px 2px}

.points{position:absolute;list-style:none;font-weight:400}
.points li{position:relative}
.points li::before{content:"•";position:absolute;left:-19px}
.s-bl .points{left:63px;top:94px;font-size:19.4px;line-height:23px;width:340px}
.s-br .points{left:53px;top:96px;font-size:21px;line-height:20.6px;width:470px}
.s-br .points li{margin-bottom:6px}

.coins{position:absolute;left:176px;top:176px;width:370px;height:212px;
  background:linear-gradient(180deg,rgba(238,241,244,0) 0%,#d9c9a2 55%,#c9ae6e 80%,#e7e1d4 100%)}

.brand{position:absolute;left:440px;top:32px;width:100px;text-align:center;
  font-size:12.2px;font-weight:700;letter-spacing:.8px;color:#2c3a3f}
.brand small{display:block;font-size:5.2px;letter-spacing:.2px;color:var(--gold);font-weight:600;margin-top:1px}
</style>
</head>
<body>

<section class="slide s-tl">
  <div class="backdrop" role="img" aria-label="Soft world map backdrop in pale blue"></div>
  <h2 class="band band-sim">Simulated Performance – under our average price discount/premium (8%)</h2>
  <div class="chart">
    <svg width="194" height="141" viewBox="0 0 194 141">
      <rect x="28" y="8" width="150" height="112" fill="#fff" stroke="#888" stroke-width=".5"/>
      <path d="M30 118 C34 80 36 10 40 10 C44 10 48 100 60 114 L176 118" fill="none" stroke="#222" stroke-width=".8"/>
      <path d="M30 118 C38 100 44 72 50 72 C58 72 64 104 90 114 L176 118" fill="none" stroke="#222" stroke-width=".7" stroke-dasharray="3 2"/>
      <path d="M30 118 C60 90 80 10 120 10 C150 10 166 40 176 70" fill="none" stroke="#444" stroke-width=".6" stroke-dasharray="1 1.5"/>
      <rect x="66" y="126" width="112" height="13" fill="#fff" stroke="#888" stroke-width=".5"/>
      <text x="94" y="132" font-size="4" fill="#333">monthly</text>
      <text x="150" y="132" font-size="4" fill="#333">quarterly</text>
      <text x="94" y="137" font-size="4" fill="#333">annual</text>
      <text x="100" y="124" font-size="4" fill="#333">% return</text>
    </svg>
  </div>
  <ul class="facts">
    <li>Mean simulated annual return is 302%</li>
    <li>Only 1% of simulated annual returns are lower than 25.7%</li>
    <li>The mean 3-year and 5-year simulated returns are 6,109% and 96,093%.</li>
    <li>The worst simulated 3-year return out of 10,000 simulated observations is +88%.</li>
    <li>The worst simulated 5-year return out of 10,000 simulated observations is +1,048%.</li>
  </ul>
  <div class="stats">
    <table>
      <colgroup><col style="width:72px"><col><col><col><col><col><col><col><col><col><col style="width:54px"><col style="width:32px"></colgroup>
      <thead>
        <tr><th colspan="12">Percentiles</th></tr>
        <tr class="cols"><th>period</th><th>mean</th><th>1%</th><th>10%</th><th>25%</th><th>50%</th><th>75%</th><th>90%</th><th>99%</th><th>min</th><th>max</th><th>% +</th></tr>
      </thead>
      <tbody>
        <tr><td class="period">monthly</td><td class="hl">11.3</td><td>(13.0)</td><td>(5.7)</td><td>0.2</td><td class="hl">8.6</td><td>19.4</td><td>31.6</td><td>58.5</td><td>(19.3)</td><td>118.8</td><td class="hl">76%</td></tr>
        <tr><td class="period">quarterly</td><td class="hl">37.4</td><td>(15.5)</td><td>1.2</td><td>13.8</td><td class="hl">31.8</td><td>55.1</td><td>80.5</td><td>137.7</td><td>(28.5)</td><td>292.2</td><td class="hl">91%</td></tr>
        <tr><td class="period">1 year</td><td class="hl">302.0</td><td class="hl">25.7</td><td>96.1</td><td>155.1</td><td class="hl">251.8</td><td>394.1</td><td>563.2</td><td>1,040.7</td><td class="hl">(27.7)</td><td>2,251.7</td><td class="hl">99.8%</td></tr>
        <tr><td class="period">3 year</td><td class="hl">6,109.3</td><td class="hl">634.2</td><td>1,511.5</td><td>2,455.8</td><td class="hl">4,291.1</td><td>7,576.9</td><td>12,373.8</td><td>31,693.1</td><td class="hl">88.4</td><td>85,014.2</td><td class="hl">100%</td></tr>
        <tr><td class="period">5 year</td><td class="hl">96,093.4</td><td class="hl">5,128.6</td><td>14,450.8</td><td>27,087.3</td><td class="hl">54,222.7</td><td>112,032.5</td><td>212,569.1</td><td>660,578.3</td><td class="hl">1,047.8</td><td>2,173,490.8</td><td class="hl">100%</td></tr>
      </tbody>
    </table>
    <p class="note">Assumes 8% price discount per trade and liquid markets. The table shows returns expressed as a percentage of the initial investment, by the amount of time since the investment period began. Each row shows estimated returns distributions using Monte Carlo simulation and bootstrapping methods. The estimates are drawn from simulated samples containing 10,000 observations for each return. <b>The simulated returns do not account for fees and taxes, which may reduce an investor's actual returns.</b></p>
  </div>
  <div class="base"></div>
</section>

<section class="slide s-tr">
  <div class="backdrop" role="img" aria-label="Soft world map backdrop in pale blue"></div>
  <h2 class="band band-sim">Simulated Performance – under a more conservative assumed price discount/premium (5%)</h2>
  <div class="chart">
    <svg width="195" height="138" viewBox="0 0 195 138">
      <rect x="28" y="8" width="150" height="110" fill="#fff" stroke="#888" stroke-width=".5"/>
      <path d="M30 116 C34 70 38 12 42 12 C46 12 52 100 64 112 L176 116" fill="none" stroke="#222" stroke-width=".8"/>
      <path d="M30 116 C36 96 42 60 48 60 C56 60 62 102 90 112 L176 116" fill="none" stroke="#222" stroke-width=".7" stroke-dasharray="3 2"/>
      <path d="M30 116 C44 80 56 14 74 14 C100 14 130 90 176 110" fill="none" stroke="#444" stroke-width=".6" stroke-dasharray="1 1.5"/>
      <rect x="66" y="122" width="112" height="13" fill="#fff" stroke="#888" stroke-width=".5"/>
      <text x="94" y="128" font-size="4" fill="#333">monthly</text>
      <text x="150" y="128" font-size="4" fill="#333">quarterly</text>
      <text x="94" y="133" font-size="4" fill="#333">annual</text>
      <text x="100" y="121" font-size="4" fill="#333">% return</text>
    </svg>
  </div>
  <ul class="facts">
    <li>Mean simulated annual return is 129%</li>
    <li>1% of the time, annual simulated returns are lower than -29.5%</li>
    <li>The mean 3-year and 5-year simulated returns are 1,129% and 6,759%.</li>
    <li>Only 1% of 5-year returns fall below +216%</li>
    <li>The worst simulated 5-year return out of 10,000 simulated observations is -16%.</li>
  </ul>
  <div class="stats">
    <table>
      <colgroup><col style="width:72px"><col><col><col><col><col><col><col><col><col><col style="width:54px"><col style="width:32px"></colgroup>
      <thead>
        <tr><th colspan="12">Percentiles</th></tr>
        <tr class="cols"><th>period</th><th>mean</th><th>1%</th><th>10%</th><th>25%</th><th>50%</th><th>75%</th><th>90%</th><th>99%</th><th>min</th><th>max</th><th>% +</th></tr>
      </thead>
      <tbody>
        <tr><td class="period">monthly</td><td>6.7</td><td>(17.4)</td><td>(10.0)</td><td>(4.0)</td><td>4.3</td><td>15.1</td><td>26.2</td><td>51.8</td><td>(22.7)</td><td>100.0</td><td>63%</td></tr>
        <tr><td class="period">quarterly</td><td class="hl">21.6</td><td>(25.7)</td><td>(10.9)</td><td>0.6</td><td class="hl">16.9</td><td>37.1</td><td>59.9</td><td>114.1</td><td>(37.8)</td><td>200.8</td><td class="hl">76%</td></tr>
        <tr><td class="period">1 year</td><td class="hl">129.2</td><td class="hl">(29.5)</td><td>12.2</td><td>46.7</td><td class="hl">100.3</td><td>178.0</td><td>280.4</td><td>555.1</td><td>(62.1)</td><td>1,403.4</td><td class="hl">94%</td></tr>
        <tr><td class="period">3 year</td><td class="hl">1,129.3</td><td class="hl">37.1</td><td>198.8</td><td>390.7</td><td class="hl">750.0</td><td>1,408.6</td><td>2,436.3</td><td>6,122.8</td><td>(67.0)</td><td>21,804.0</td><td class="hl">99.7%</td></tr>
        <tr><td class="period">5 year</td><td class="hl">6,759.0</td><td class="hl">216.5</td><td>816.4</td><td>1,636.4</td><td class="hl">3,523.6</td><td>7,368.2</td><td>14,846.8</td><td>52,779.2</td><td class="hl">(15.9)</td><td>260,998.3</td><td class="hl">99.97%</td></tr>
      </tbody>
    </table>
    <p class="note">Assumes 5% price discount per trade and liquid markets. The table shows returns expressed as a percentage of the initial investment, by the amount of time since the investment period began. Each row shows estimated returns distributions using Monte Carlo simulation and bootstrapping methods. The estimates are drawn from simulated samples containing 10,000 observations for each return. <b>The simulated returns do not account for fees and taxes, which may reduce an investor's actual returns.</b></p>
  </div>
  <div class="base"></div>
</section>

<section class="slide s-bl">
  <div class="backdrop"></div>
  <h2 class="band band-big">Actual Performance</h2>
  <ul class="points">
    <li>The fund will launch in May 2016.</li>
    <li>We will report fund performance on a monthly basis starting in June.</li>
  </ul>
  <div class="coins" role="img" aria-label="Photo of rising stacks of gold coins"></div>
  <div class="base"></div>
</section>

<section class="slide s-br">
  <div class="backdrop" role="img" aria-label="Soft world map backdrop in pale blue"></div>
  <h2 class="band band-big">Risk Management</h2>
  <div class="brand">ALDERLINE<small>CAPITAL MANAGEMENT LLC</small></div>
  <ul class="points">
    <li>Our top priority is safety</li>
    <li>If the market does not offer a price discount or premium, we trade at the best available price to stay within our trading parameters.</li>
    <li>This approach minimizes losses in illiquid markets.</li>
    <li>The simulated strategy performance at substantially lower average price discount/ premium, relative to the average we have achieved to date, exhibits limited downside risk (see simulation results at 5% versus 8% discount/premium)</li>
  </ul>
  <div class="base"></div>
</section>

</body>
</html>
```